Unique Builder wordpress website - Supply Graphics Only

We need a brand new website for a building company in Perth, Australia who constructs insulated panels (sip).
What is a SIP?
A SIP is a high-performance building panel used for floors, walls, and roofs in residential and commercial buildings. Panels are typically made using Expanded Polystyrene (EPS) sandwiched between two structural skins.
The design must incorporate a slick professional look and keep to the logo colours (Lime green & Blacks). The logo must not change colours or be altered. (
We will convert the graphics to a wordpress site. We have our own coders)
Design:
The website design must be clean, mobile friendly and the final design will be adapted to WordPress CMS.
The menus must contain dropdown menus and front page may contain a youtube video at a later date.
Fonts must be clear and easy to read
The contact us page will need to have an online form and google map.
The 16 pages listed will be the complete site and are for reference only. For this project the winning designer would need to supply the Homepage, and 1 inner pages only as PSD files.
The structure is as follows:
Home
About us
High Tech Homes
What is a sip
Benefits
FAQ
Designs
Residential
Granny Flats
Architectural design
Photo Gallery <--- Would be great if a sample design can be provided
Services
Project management and custom design
Site Assembly
Kit Supply
Contact us
***We don't need the designer to design every page however a 1 inner page would be ideal****
Our Competitors websites
Note: the following websites look crap however, the following websites are some of our competitors. We want a clean and awesome layout.
http://www.vorkalite.com.au/
http://trenmoreworks.com.au/
http://www.bralvexa.net.au/
New home builders and commercial builders
Building
5+ page

```html
<!DOCTYPE html>
<html lang="en">
<head>
<meta charset="utf-8">
<title>Corvane – Structural Insulated Panels</title>
<link href="https://fonts.googleapis.com/css2?family=Open+Sans:wght@400;600;700&display=swap" rel="stylesheet">
<style>
  :root {
    --page-bg: #f1f9fc;
    --white: #ffffff;
    --lime: #a8c72f;
    --lime-bright: #b5d334;
    --ink: #1e1e1e;
    --body-text: #4a4a4a;
    --muted-text: #5e5e5e;
    --panel-grey: #f3f3f3;
    --hero-dark: #3b2c1c;
    --hero-mid: #8a6a45;
    --hero-light: #cdb795;
    --caption-yellow: #e4d21c;
    --tick-yellow: #f3e43a;
    --video-black: #060606;
    --video-bar: #2a2a2a;
    --video-icon: #d8d8d8;
  }
  * { box-sizing: border-box; margin: 0; padding: 0; }
  html, body { width: 1200px; height: 873px; overflow: hidden; }
  body {
    background: var(--page-bg);
    font-family: "Open Sans", Arial, sans-serif;
    color: var(--body-text);
    position: relative;
  }
  .site {
    position: absolute;
    left: 160px;
    top: 10px;
    width: 880px;
    height: 863px;
    background: var(--white);
    overflow: hidden;
  }
  .site-header {
    height: 76px;
    display: flex;
    align-items: center;
    justify-content: space-between;
    padding-left: 12px;
  }
  .brand { display: flex; align-items: center; gap: 10px; }
  .brand-mark { width: 22px; height: 22px; background: var(--ink); }
  .brand-name { font-size: 20px; font-weight: 600; color: var(--ink); letter-spacing: -0.3px; }
  .main-nav { display: flex; height: 100%; }
  .main-nav a {
    display: flex; align-items: center;
    padding: 0 20px;
    font-size: 12px; font-weight: 600;
    color: var(--ink); text-decoration: none;
  }
  .main-nav a.is-active { background: var(--lime-bright); color: var(--white); width: 72px; justify-content: center; padding: 0; }
  .hero {
    position: relative;
    height: 376px;
    background:
      radial-gradient(ellipse at 30% 45%, var(--hero-light) 0%, transparent 45%),
      linear-gradient(120deg, var(--hero-mid) 0%, var(--hero-light) 40%, var(--hero-mid) 65%, var(--hero-dark) 100%);
  }
  .hero-caption {
    position: absolute;
    left: 17px; top: 250px;
    width: 270px;
    background: rgba(228, 210, 28, 0.85);
    padding: 5px 6px;
    font-size: 14.5px; line-height: 22px;
    text-align: justify;
    color: var(--ink);
  }
  .hero-caption strong { font-weight: 700; }
  .content { position: relative; height: 411px; margin-top: 38px; }
  .intro {
    position: absolute; left: 10px; top: 0;
    width: 417px; height: 100%;
    background: var(--panel-grey);
    padding: 17px 14px 0 28px;
  }
  .intro p { font-size: 14.5px; line-height: 22.5px; text-align: justify; letter-spacing: 0.3px; }
  .intro p + p { margin-top: 48px; }
  .intro p.small { font-size: 13px; color: var(--muted-text); }
  .intro .name { font-weight: 700; color: var(--ink); font-size: 16px; letter-spacing: 1px; }
  .intro .name-lead { color: var(--lime); }
  .benefits {
    position: absolute; left: 450px; top: 0;
    width: 418px; height: 228px;
    background: var(--lime);
    padding: 16px 24px 0 18px;
    list-style: none;
    color: var(--white);
    font-size: 14px; line-height: 22.5px;
  }
  .benefits li { position: relative; text-indent: 22px; }
  .benefits svg { position: absolute; left: 0; top: 5px; width: 13px; height: 13px; }
  .video {
    position: absolute; left: 450px; top: 250px;
    width: 418px; height: 200px;
    background: var(--video-black);
  }
  .video-bar { height: 18px; background: var(--video-bar); display: flex; justify-content: flex-end; align-items: center; gap: 6px; padding-right: 8px; }
  .video-bar span { width: 7px; height: 7px; border-radius: 50%; background: var(--video-icon); }
  .video-play { position: absolute; left: 197px; top: 104px; width: 24px; height: 28px; }
</style>
</head>
<body>
  <div class="site">
    <header class="site-header">
      <div class="brand">
        <span class="brand-mark"></span>
        <span class="brand-name">Corvane</span>
      </div>
      <nav class="main-nav">
        <a href="#" class="is-active">Home</a>
        <a href="#">Service</a>
        <a href="#">Benifit</a>
        <a href="#">About Us</a>
      </nav>
    </header>

    <section class="hero" role="img" aria-label="Sepia photograph of an ornate street clock in front of a tall historic building">
      <p class="hero-caption"><strong>Corvane</strong> are designers and manufacturers of an engineered structural insulated panel and concealed structural frame build-</p>
    </section>

    <section class="content">
      <div class="intro">
        <p><span class="name"><span class="name-lead">Corv</span>ane</span> are designers and manufacturers of an engineered structural insulated panel and concealed structural frame building product.</p>
        <p>sips is rapidly becoming the building method of choice because of its overwhelming benefits and proven suitability.</p>
        <p class="small"><span class="name"><span class="name-lead">Corv</span>ane</span> panels can be used in residential and commercial building and are fully compliant to Australian standards.</p>
        <p class="small">We specialize in supplying on time and on budget, with high</p>
      </div>

      <ul class="benefits">
        <li><svg viewBox="0 0 12 12"><path d="M1 6.5l3 3 7-7" fill="none" stroke="var(--tick-yellow)" stroke-width="2.2"/></svg>High level of captive insulation. (warm in winter cool in summer)</li>
        <li><svg viewBox="0 0 12 12"><path d="M1 6.5l3 3 7-7" fill="none" stroke="var(--tick-yellow)" stroke-width="2.2"/></svg>Very strong, light weight and durable.</li>
        <li><svg viewBox="0 0 12 12"><path d="M1 6.5l3 3 7-7" fill="none" stroke="var(--tick-yellow)" stroke-width="2.2"/></svg>20 + year history of performance in cyclonic locations in WA</li>
        <li><svg viewBox="0 0 12 12"><path d="M1 6.5l3 3 7-7" fill="none" stroke="var(--tick-yellow)" stroke-width="2.2"/></svg>Reduced build time (save time save money it's that easy)</li>
        <li><svg viewBox="0 0 12 12"><path d="M1 6.5l3 3 7-7" fill="none" stroke="var(--tick-yellow)" stroke-width="2.2"/></svg>Energy efficient ( less energy to build and less energy to run ie lower power bills)</li>
      </ul>

      <div class="video" role="img" aria-label="Embedded video player">
        <div class="video-bar"><span></span><span></span></div>
        <svg class="video-play" viewBox="0 0 24 28"><path d="M2 2l20 12-20 12z" fill="var(--video-icon)"/></svg>
      </div>
    </section>
  </div>
</body>
</html>
```